Two Rollup Banners Promoting Trade Association

UPDATE: Please do not recycle the prior designs we've had. I am looking for creativity and a new look. Otherwise, I would use the prior designers to just update their work.
I need two 48"x79" Pull Up Retractable Banners Designed.
One promotes the benefits of membership in the Residential Capital Partners Forum. The second promotes RCPF's role in the affordable housing ecosystem.
The content for each is attached. I'm also providing examples of two banners we recently created for our 30th Anniversary as well as some photos of our members if you choose to use them (although it's not necessary - just providing them as an option).
The banners don't have to mimic the ones we did for our 30th Anniversary. I'm simply providing them as examples of designs that meet the look and feel of our brand.
I've also provided our brand guidelines and the specs for the banner.
Updates
All,
We are looking for clean, modern, streamlined designs. No clip art. No waves. Don’t bury the message in the graphics.
Please keep that in mind as you submit designs.
Look and feel
Each slider illustrates characteristics of the customer's brand and the style your logo design should communicate.

```html
<!DOCTYPE html>
<html lang="en">
<head>
<meta charset="utf-8">
<title>RCPF – LIHTC Investor-Only Community</title>
<link rel="stylesheet" href="https://fonts.googleapis.com/css2?family=Montserrat:wght@300;400;700;800&family=Hind:wght@300;400&display=swap">
<style>
  :root {
    --orange: #f94f0c;
    --orange-soft: #f7b59a;
    --ink: #141414;
    --slate: #566069;
    --body: #4a4a4a;
    --seg-1: #f2f3f5;
    --seg-2: #e8e9ec;
    --seg-3: #dfe0e3;
    --white: #ffffff;
    --page: #fbfbfc;
  }
  * { margin: 0; padding: 0; box-sizing: border-box; }
  html, body { width: 728px; height: 1200px; overflow: hidden; background: var(--page); }
  .banner {
    position: relative;
    width: 728px;
    height: 1200px;
    overflow: hidden;
    background: var(--page);
    font-family: "Hind", "Helvetica Neue", Arial, sans-serif;
    color: var(--body);
  }
  .abs { position: absolute; }
  .center-x { transform: translateX(-50%); text-align: center; white-space: nowrap; }

  /* Brand */
  .brand { left: 78px; top: 40px; display: flex; align-items: center; gap: 14px; }
  .brand-mark { width: 46px; height: 46px; background: var(--orange); }
  .brand-name {
    font-family: "Montserrat", Arial, sans-serif;
    font-weight: 700; font-size: 56px; line-height: 1;
    color: var(--slate); letter-spacing: -1px;
  }
  .brand-full {
    font-family: "Montserrat", Arial, sans-serif;
    font-weight: 700; font-size: 10.5px; line-height: 1.15;
    color: var(--slate); letter-spacing: 0.6px; text-transform: uppercase;
    width: 110px; padding-left: 12px; border-left: 1px solid #c9ccd0;
  }

  .top-band, .rows { left: 0; top: 0; }

  /* Hero photo area */
  .hero {
    left: 0; top: 131px; width: 728px; height: 330px;
    background:
      radial-gradient(ellipse at 30% 55%, rgba(248, 196, 170, 0.55), transparent 55%),
      linear-gradient(180deg, #aab5d6 0%, #c3c8df 35%, #dcd6e2 60%, #f4f1f3 80%, var(--page) 100%);
  }

  /* Title pill */
  .title-pill {
    left: 81px; top: 356px; width: 566px; height: 90px;
    background: var(--orange); border-radius: 32px;
    color: var(--white); text-align: center;
    font-family: "Montserrat", Arial, sans-serif;
    padding-top: 10px;
  }
  .title-pill .title-strong { font-weight: 700; font-size: 29px; letter-spacing: 2.5px; line-height: 36px; }
  .title-pill .title-light { font-weight: 300; font-size: 29px; letter-spacing: 3px; line-height: 36px; }

  .section-heading {
    font-family: "Montserrat", Arial, sans-serif;
    font-weight: 800; font-size: 29px; letter-spacing: 3px;
    color: var(--ink); line-height: 1;
  }

  /* Benefit items */
  .benefit { transform: translateX(-50%); text-align: center; white-space: nowrap; }
  .benefit-title {
    font-family: "Montserrat", Arial, sans-serif;
    font-weight: 700; font-size: 20px; letter-spacing: 2px;
    color: var(--orange); line-height: 24px;
  }
  .benefit-text { font-weight: 300; font-size: 20.5px; line-height: 25.5px; color: var(--body); }

  /* Stats */
  .stat-figure {
    font-family: "Montserrat", Arial, sans-serif;
    font-weight: 700; color: var(--orange); line-height: 1;
  }
  .stat-text { font-weight: 300; font-size: 20.5px; line-height: 25.3px; color: var(--body); }
  .stat-divider { left: 327px; top: 838px; width: 1px; height: 120px; background: var(--orange-soft); }

  /* Calls to action */
  .cta-join {
    left: 208px; top: 998px; width: 313px; height: 51px;
    background: var(--orange); border-radius: 18px;
    color: var(--white); font-family: "Montserrat", Arial, sans-serif;
    font-weight: 300; font-size: 21px; letter-spacing: 3px;
    display: flex; align-items: center; justify-content: center;
  }
  .cta-web {
    left: 208px; top: 1054px; width: 313px; height: 51px;
    background: var(--white); border: 1px solid var(--orange-soft); border-radius: 18px;
    display: flex; align-items: center; justify-content: center; gap: 8px;
    font-family: "Montserrat", Arial, sans-serif; font-weight: 800;
    font-size: 17px; letter-spacing: 1.5px; color: var(--ink);
  }
  .bottom-band { left: 0; top: 1168px; width: 728px; height: 32px; background: var(--orange); }
</style>
</head>
<body>
<main class="banner">

  <header class="brand abs">
    <span class="brand-mark"></span>
    <span class="brand-name">RCPF</span>
    <span class="brand-full">Residential Capital Partners Forum</span>
  </header>

  <div class="hero abs" role="img" aria-label="Photograph of a suburban house with gabled roofs at dusk under a soft lavender sky"></div>

  <svg class="top-band abs" width="728" height="140" viewBox="0 0 728 140" aria-hidden="true">
    <polygon points="0,127 728,117 728,131 0,131" fill="var(--orange)"/>
  </svg>

  <div class="title-pill abs">
    <div class="title-strong">LIHTC INVESTOR-ONLY</div>
    <div class="title-light">COMMUNITY</div>
  </div>

  <h2 class="section-heading abs center-x" style="left:358px; top:468px;">WHERE INVESTORS</h2>

  <svg class="rows abs" width="728" height="780" viewBox="0 0 728 780" aria-hidden="true">
    <polygon points="418,521 728,521 728,637 418,637 433,579" fill="var(--seg-3)"/>
    <polygon points="250,521 418,521 433,579 418,637 250,637 265,579" fill="var(--seg-2)"/>
    <polygon points="0,521 250,521 265,579 250,637 0,637" fill="var(--seg-1)"/>
    <polygon points="294,647 617,647 674,705 617,763 294,763 309,705" fill="var(--seg-3)"/>
    <polygon points="0,647 294,647 309,705 294,763 0,763" fill="var(--seg-2)"/>
  </svg>

  <div class="benefit abs" style="left:131px; top:542px;">
    <div class="benefit-title">NETWORK</div>
    <div class="benefit-text">Peer Groups<br>&amp; Forums</div>
  </div>
  <div class="benefit abs" style="left:341px; top:542px;">
    <div class="benefit-title">LEARN</div>
    <div class="benefit-text">Conferences<br>&amp; Webinars</div>
  </div>
  <div class="benefit abs" style="left:554px; top:542px;">
    <div class="benefit-title">SHARE</div>
    <div class="benefit-text">Candid Investor-Only<br>Exchange</div>
  </div>
  <div class="benefit abs" style="left:155px; top:668px;">
    <div class="benefit-title">SHAPE</div>
    <div class="benefit-text">Industry Standards<br>&amp; Best Practices</div>
  </div>
  <div class="benefit abs" style="left:484px; top:668px;">
    <div class="benefit-title">GROW</div>
    <div class="benefit-text">Professional Development<br>&amp; Emerging Leaders Program</div>
  </div>

  <h2 class="section-heading abs center-x" style="left:363px; top:785px;">OUR COMMUNITY</h2>

  <div class="stat abs center-x" style="left:200px; top:869px;">
    <div class="stat-figure" style="font-size:35px;">60+</div>
    <div class="stat-text" style="margin-top:4px;">Investor Firms</div>
  </div>

  <div class="stat-divider abs"></div>

  <div class="stat abs center-x" style="left:489px; top:835px;">
    <div class="stat-figure" style="font-size:40px;">1,000+</div>
    <div class="stat-text" style="margin-top:2px;">Industry Professionals<br>Banks (Large &amp; Small),<br>Insurance Companies,<br>Economic Investors</div>
  </div>

  <div class="cta-join abs">JOIN US TODAY</div>

  <div class="cta-web abs">
    <svg width="20" height="20" viewBox="0 0 20 20" aria-hidden="true">
      <circle cx="10" cy="10" r="8" fill="none" stroke="var(--orange)" stroke-width="2"/>
      <ellipse cx="10" cy="10" rx="3.5" ry="8" fill="none" stroke="var(--orange)" stroke-width="1.5"/>
      <line x1="2" y1="10" x2="18" y2="10" stroke="var(--orange)" stroke-width="1.5"/>
    </svg>
    <span>WWW.RCPFORUM.ORG</span>
  </div>

  <div class="bottom-band abs"></div>
</main>
</body>
</html>
```